Dorian Felsgrove breaking. Or D. Felsgrove breaking

I break in and train horses, any age any bread of horse, for any disaplin. I need a business card that is simple but effective, in the way of looking professional. I would like a horse on my card, preferably a horse without a rider. I also pre train horse, younge horses that need a bit of riding before they go into serious work, and prepare yearlings for sale.

Reason: This is for my boyfriend, and I really want it to be perfect and impressive!

Target Market(s)

Thoroughbred race horse trainers, horse industrie people.

Industry/Entity Type

Business

Contact Information for Business Card

Dorian Felsgrove horse breaking, "WOLBUNDA" Kellowan, give your horse the right start to any career. dfels@quillmail.com.au, 0431862097. Horse breaking~pre-training~sale preparation

```html
<!DOCTYPE html>
<html lang="en">
<head>
<meta charset="utf-8">
<title>Dorian Felsgrove – Business Card</title>
<link href="https://fonts.googleapis.com/css2?family=Caveat:wght@500;600&family=Titillium+Web:wght@300;400;600&display=swap" rel="stylesheet">
<style>
  :root {
    --page-bg: #d9d9d9;
    --card-top: #1c1410;
    --card-mid: #3a2a20;
    --card-bottom: #8a7260;
    --text-light: #f4efe9;
    --text-muted: #d8cfc6;
    --tagline: #2a1c14;
    --art-tone-a: rgba(120, 95, 75, 0.0);
    --art-tone-b: rgba(150, 120, 95, 0.35);
  }
  html, body {
    margin: 0;
    width: 1200px;
    height: 861px;
    overflow: hidden;
    background: var(--page-bg);
  }
  .canvas {
    position: relative;
    width: 1200px;
    height: 861px;
  }
  .business-card {
    position: absolute;
    left: 150px;
    top: 173px;
    width: 900px;
    height: 514px;
    background: linear-gradient(180deg, var(--card-top) 0%, var(--card-mid) 50%, var(--card-bottom) 100%);
    box-shadow: 0 18px 40px rgba(0,0,0,0.35);
    overflow: hidden;
  }
  .horse-art {
    position: absolute;
    right: 0;
    top: 0;
    width: 440px;
    height: 400px;
    background: radial-gradient(ellipse at 55% 45%, var(--art-tone-b) 0%, var(--art-tone-a) 70%);
  }
  .card-name {
    position: absolute;
    left: 52px;
    top: 44px;
    margin: 0;
    font-family: "Caveat", cursive;
    font-weight: 600;
    font-size: 62px;
    line-height: 1.2;
    color: var(--text-light);
    letter-spacing: 1px;
  }
  .card-services {
    position: absolute;
    left: 54px;
    top: 126px;
    margin: 0;
    font-family: "Titillium Web", sans-serif;
    font-weight: 300;
    font-size: 15px;
    letter-spacing: 0.5px;
    color: var(--text-muted);
  }
  .card-role {
    position: absolute;
    left: 54px;
    top: 152px;
    margin: 0;
    font-family: "Titillium Web", sans-serif;
    font-weight: 600;
    font-size: 25px;
    color: var(--text-light);
  }
  .contact-list {
    position: absolute;
    left: 52px;
    top: 222px;
    margin: 0;
    padding: 0;
    list-style: none;
  }
  .contact-item {
    display: flex;
    align-items: center;
    height: 50px;
    font-family: "Titillium Web", sans-serif;
    font-weight: 400;
    font-size: 23px;
    color: var(--text-light);
  }
  .contact-icon {
    width: 28px;
    height: 28px;
    margin-right: 8px;
    flex: none;
  }
  .card-tagline {
    position: absolute;
    left: 44px;
    top: 418px;
    margin: 0;
    font-family: "Caveat", cursive;
    font-weight: 500;
    font-size: 46px;
    color: var(--tagline);
    letter-spacing: 1px;
    white-space: nowrap;
  }
</style>
</head>
<body>
<main class="canvas">
  <section class="business-card">
    <div class="horse-art" role="img" aria-label="Sketched horse head in a bridle, facing left"></div>

    <h1 class="card-name">Dorian Felsgrove</h1>
    <p class="card-services">HORSE BREAKING • PRE-TRAINING • SALE PREPARATION</p>
    <p class="card-role">Trainer</p>

    <ul class="contact-list">
      <li class="contact-item">
        <svg class="contact-icon" viewBox="0 0 28 28" aria-hidden="true">
          <circle cx="14" cy="14" r="12.5" fill="none" stroke="#f4efe9" stroke-width="2"/>
          <path d="M7 14 L14 8 L21 14 M9.5 12.5 V20 H18.5 V12.5" fill="none" stroke="#f4efe9" stroke-width="2" stroke-linejoin="round"/>
        </svg>
        Wolbunda, Kellowan
      </li>
      <li class="contact-item">
        <svg class="contact-icon" viewBox="0 0 28 28" aria-hidden="true">
          <circle cx="14" cy="14" r="12.5" fill="none" stroke="#f4efe9" stroke-width="2"/>
          <path d="M9 19 L18 10 L20 12 L11 21 L8.5 21.5 Z" fill="#f4efe9"/>
        </svg>
        0431862097
      </li>
      <li class="contact-item">
        <svg class="contact-icon" viewBox="0 0 28 28" aria-hidden="true">
          <circle cx="14" cy="14" r="12.5" fill="none" stroke="#f4efe9" stroke-width="2"/>
          <rect x="7.5" y="9.5" width="13" height="9" fill="none" stroke="#f4efe9" stroke-width="1.8"/>
          <path d="M7.5 9.5 L14 15 L20.5 9.5" fill="none" stroke="#f4efe9" stroke-width="1.8"/>
        </svg>
        dfels@quillmail.com.au
      </li>
    </ul>

    <p class="card-tagline">Give your horse the right start to any career.</p>
  </section>
</main>
</body>
</html>
```